Email Signature

We need a generic email signature designed for our buiding company called 'Willow Dwellings'.
We need the following included:
- Name
- Job title (Sales Consultant)
- Phone number
- Mobile number
- Email address
- Physical address
- Web addresss
Please look at the files I have uploaded as these will give you a good idea on our current branding. Our current email signature works well but just needs refreshing! I've also uploaded some images which can be used if needed.
Industry/Entity Type
It Company
Requirements
Nice to have
- If you could incorporate the colours used on the brochure example (contents list) and and arrows on the bottom of the letterhead... just a thought!

```html
<!DOCTYPE html>
<html lang="en">
<head>
<meta charset="utf-8">
<title>Willow Dwellings – Email Signature</title>
<link rel="stylesheet" href="https://fonts.googleapis.com/css2?family=Montserrat:wght@300;400;600;700&display=swap">
<style>
  :root {
    --navy: #2d2b55;
    --brand-red: #a0171f;
    --white: #ffffff;
    --taupe: #5a4c4b;
    --plum: #5e1c4c;
  }
  html, body {
    margin: 0;
    padding: 0;
    width: 1200px;
    height: 800px;
    overflow: hidden;
    background: var(--navy);
  }
  .signature {
    position: relative;
    width: 1200px;
    height: 800px;
    background: var(--navy);
    font-family: "Montserrat", sans-serif;
    color: var(--white);
  }
  .band { position: absolute; left: 0; width: 1200px; }
  .band--rule-top { top: 75px; height: 10px; background: var(--brand-red); }
  .band--header { top: 85px; height: 106px; background: var(--white); }
  .band--rule-bottom { top: 191px; height: 10px; background: var(--brand-red); }

  .brand {
    position: absolute;
    top: 103px;
    right: 52px;
    height: 73px;
    display: flex;
    align-items: center;
    gap: 22px;
  }
  .brand__mark {
    width: 73px;
    height: 73px;
    background: var(--brand-red);
  }
  .brand__name {
    font-size: 56px;
    font-weight: 600;
    color: var(--brand-red);
    letter-spacing: -0.5px;
    line-height: 1;
    white-space: nowrap;
  }

  .person {
    position: absolute;
    left: 127px;
    top: 278px;
  }
  .person__name {
    margin: 0;
    font-size: 35px;
    font-weight: 700;
    line-height: 1.25;
  }
  .person__title {
    margin: 0;
    font-size: 35px;
    font-weight: 300;
    line-height: 1.3;
  }

  .contact {
    position: absolute;
    right: 47px;
    top: 443px;
    margin: 0;
    padding: 0;
    list-style: none;
    text-align: right;
    font-size: 29px;
    font-weight: 300;
    line-height: 42px;
  }
  .contact__label { font-weight: 700; }

  .stripe { position: absolute; left: 0; width: 1200px; }
  .stripe--line-1 { top: 669px; height: 5px; background: var(--white); }
  .stripe--taupe { top: 674px; height: 26px; background: var(--taupe); }
  .stripe--line-2 { top: 700px; height: 5px; background: var(--white); }
  .stripe--plum { top: 705px; height: 25px; background: var(--plum); }
  .stripe--line-3 { top: 730px; height: 5px; background: var(--white); }
  .stripe--line-4 { top: 766px; height: 5px; background: var(--white); }
</style>
</head>
<body>
  <main class="signature">
    <div class="band band--rule-top"></div>
    <div class="band band--header"></div>
    <div class="band band--rule-bottom"></div>

    <div class="brand">
      <div class="brand__mark" aria-hidden="true"></div>
      <span class="brand__name">Willow Dwellings</span>
    </div>

    <section class="person">
      <p class="person__name">Name and Lastname</p>
      <p class="person__title">Sales Consultant</p>
    </section>

    <ul class="contact">
      <li><span class="contact__label">Phone</span> 03 5550 2418</li>
      <li><span class="contact__label">Mobile</span> 0400 555 016</li>
      <li><span class="contact__label">E-mail</span> yourname@willowdwellings.com</li>
      <li><span class="contact__label">Adress</span> 18 Harbour Lane, Ashford Victoria 3790</li>
      <li><span class="contact__label">Web</span> www.willowdwellings.com</li>
    </ul>

    <div class="stripe stripe--line-1"></div>
    <div class="stripe stripe--taupe"></div>
    <div class="stripe stripe--line-2"></div>
    <div class="stripe stripe--plum"></div>
    <div class="stripe stripe--line-3"></div>
    <div class="stripe stripe--line-4"></div>
  </main>
</body>
</html>
```